A new cover photo for facebook page for our sleep clinic to highlight the launch of eStore

Need a cover photo for our fb page announcing the eStore launch. There is one currently on our page https://www.facebook.com/quillharbor.
Improve upon it. Use the supplied logo but eliminate Quill. Use the text from the current fb cover photo. You will have to do use the background photo of the product.

Target Market(s)

Males 40-60 age without insurance or with high deductible insurance

Industry/Entity Type

Clinic

Font styles to use
Sans Serif
Other font styles liked:
• the same font as it is under Quill & Harbor Clinic logo

Requirements
Must have
• HarborClinic.com
• Internet's Best CPAP Store
• Lowest Prices - Priceless Advice
Should not have
• Eliminate -
• Quill &
• The whole text starting with "Open field of vision...." in the box in the corner.

```html
<!DOCTYPE html>
<html lang="en">
<head>
<meta charset="utf-8">
<title>Harbor Clinic – Cover</title>
<link rel="stylesheet" href="https://fonts.googleapis.com/css2?family=Raleway:wght@500;600&family=Arimo:wght@700&display=swap">
<style>
  :root {
    --stage-top: #e7e7e7;
    --stage-bottom: #b8b8b8;
    --white: #ffffff;
    --pillow: #e4e7ea;
    --sheet: #c3cbd3;
    --skin-warm: #9c8478;
    --hair-dark: #4a3f3c;
    --photo-mid: #6f85a6;
    --photo-deep: #2f4f86;
    --accent-green: #4fae2d;
    --brand-blue: #2b4a8b;
    --frame-grey: #8c8c8c;
    --placeholder-text: #c4c9d6;
  }
  * { margin: 0; padding: 0; box-sizing: border-box; }
  html, body { width: 1200px; height: 1000px; overflow: hidden; }
  body {
    background: linear-gradient(180deg, var(--stage-top), var(--stage-bottom));
    position: relative;
    font-family: "Raleway", Arial, sans-serif;
  }
  .cover {
    position: absolute;
    left: 175px; top: 340px;
    width: 851px; height: 315px;
    background: var(--white);
    overflow: hidden;
  }
  .cover-photo {
    position: absolute;
    left: 0; top: 0;
    width: 721px; height: 315px;
    background:
      radial-gradient(ellipse 120px 90px at 160px 70px, rgba(74,63,60,0.75) 0%, rgba(74,63,60,0) 100%),
      radial-gradient(ellipse 110px 80px at 330px 90px, rgba(74,63,60,0.55) 0%, rgba(74,63,60,0) 100%),
      radial-gradient(ellipse 150px 110px at 230px 170px, rgba(156,132,120,0.75) 0%, rgba(156,132,120,0) 100%),
      radial-gradient(ellipse 140px 100px at 380px 180px, rgba(156,132,120,0.6) 0%, rgba(156,132,120,0) 100%),
      radial-gradient(ellipse 260px 120px at 520px 40px, rgba(228,231,234,0.95) 0%, rgba(228,231,234,0) 100%),
      radial-gradient(ellipse 220px 110px at 110px 20px, rgba(228,231,234,0.9) 0%, rgba(228,231,234,0) 100%),
      radial-gradient(ellipse 300px 120px at 330px 290px, rgba(111,133,166,0.8) 0%, rgba(111,133,166,0) 100%),
      linear-gradient(130deg, var(--sheet) 0%, var(--photo-mid) 55%, var(--photo-deep) 100%);
  }
  .cover-curve { position: absolute; left: 0; top: 0; width: 721px; height: 315px; }
  .profile-slot {
    position: absolute;
    left: 12px; top: 175px;
    width: 170px; height: 145px;
    border: 1px solid var(--frame-grey);
    background: var(--white);
    display: flex; align-items: center; justify-content: center;
    padding-top: 14px;
    font-family: "Arimo", Arial, sans-serif;
    font-weight: 700;
    font-size: 22px;
    line-height: 26px;
    letter-spacing: 1.5px;
    text-align: center;
    color: var(--placeholder-text);
  }
  .taglines {
    position: absolute;
    right: 145px; top: 213px;
    list-style: none;
    text-align: right;
  }
  .taglines li {
    font-size: 15px;
    font-weight: 500;
    letter-spacing: 1px;
    color: var(--white);
    height: 30px;
    line-height: 20px;
    display: flex; align-items: center; justify-content: flex-end;
  }
  .taglines li::after {
    content: "";
    width: 9px; height: 9px;
    border-radius: 50%;
    background: var(--white);
    margin-left: 13px;
  }
  .taglines .web-address { color: var(--accent-green); }
  .taglines .web-address::after { background: var(--accent-green); }
  .brand {
    position: absolute;
    left: 721px; top: 212px;
    width: 130px;
    display: flex; flex-direction: column; align-items: center;
    color: var(--brand-blue);
    font-weight: 600;
  }
  .brand-dot {
    width: 52px; height: 52px; border-radius: 50%;
    background: var(--accent-green);
    margin-bottom: 6px;
  }
  .brand-name { font-size: 23px; line-height: 1; }
  .brand-sub { font-size: 9px; letter-spacing: 6px; margin-top: 4px; padding-left: 6px; text-transform: uppercase; }
</style>
</head>
<body>
  <section class="cover">
    <div class="cover-photo" role="img" aria-label="Photo of a couple sleeping peacefully on white pillows, the man wearing a CPAP nasal mask"></div>
    <svg class="cover-curve" viewBox="0 0 721 315" aria-hidden="true">
      <path d="M0 0 L15 0 C 75 120, 175 245, 343 315 L0 315 Z" fill="#ffffff"/>
    </svg>
    <div class="profile-slot">Profile<br>Photo</div>
    <ul class="taglines">
      <li>Internet's Best CPAP Store</li>
      <li>Lowest Prices - Priceless Advice</li>
      <li class="web-address">www.HarborClinic.com</li>
    </ul>
    <div class="brand">
      <span class="brand-dot"></span>
      <span class="brand-name">Harbor</span>
      <span class="brand-sub">Clinic</span>
    </div>
  </section>
</body>
</html>
```